Brantwell College Course Brochure

Brantwell College is a private institution providing different courses for students internationally.
We need a series of brochures for 5 new courses individually.(5 pieces in total)
We have opened 5 courses
1. Higher Diploma in Construction & Civil engineering
2.Higher Diploma in Quantity Surveying
3.Higher Diploma in Mechanical Engineering
4.Higher Diploma in Electrical & Electronic Engineering
5.Higher Diploma in Facilities Management

Please give out the design sample using one of the course, then drag and adjust accordingly for other courses

Requirement
*Vibrant and energetic looking
*Size A5 double sided/A4 size double fold
*Please include the given company logo and Learnsafe image
*Refer to "Higher Diploma synopsis" file for course description
*information must be clear to see
*Entry requirements modules and other course details must be included in
*Redesign according to the attached files
* a PSD file is attached for reference and obtain information

Target Market(s)

International students above 21 years old

Industry/Entity Type

Education

Font styles to use
Sans Serif

Requirements
Must have
• *Please include the given company logo and Learnsafe image
• *Summarise the descriptions, do not be wordy.
• *information must be clear to see
• *Entry requirements modules and other course details must be included in
• *attached file for reference
Nice to have
• More catchy images and designs
• Keep it simple
• It is on designer's choice of color, does not have to use only company colours.

```html
<!DOCTYPE html>
<html lang="en">
<head>
<meta charset="utf-8">
<title>Brantwell College – Higher Diploma in Mechanical Engineering</title>
<link rel="stylesheet" href="https://fonts.googleapis.com/css2?family=Montserrat:wght@700;800&family=Ubuntu:ital,wght@0,400;0,500;0,700;1,400&family=Tinos:wght@400;700&display=swap">
<style>
:root{
  --navy:#1b2266;
  --navy-deep:#121a52;
  --orange:#f5a224;
  --orange-deep:#e48a12;
  --orange-soft:#fcd592;
  --row-grey:#f0f0f0;
  --ink:#2a2a2a;
  --page:#ffffff;
  --backdrop:#d9d9d9;
}
*{margin:0;padding:0;box-sizing:border-box}
html,body{width:1200px;height:960px;overflow:hidden;background:var(--backdrop)}
body{font-family:"Ubuntu",sans-serif;color:var(--ink);position:relative}
.sheet{position:absolute;left:16px;top:64px;width:1358px;height:968px;transform:scale(.86);transform-origin:0 0;background:var(--page)}
.abs{position:absolute}

/* left page */
.cover{position:absolute;left:0;top:0;width:679px;height:968px;overflow:hidden}
.hero-art{position:absolute;left:0;top:0}
.brand{position:absolute;left:505px;top:28px;width:160px;text-align:center}
.brand-dot{width:78px;height:78px;border-radius:50%;background:var(--navy);margin:0 auto 10px}
.brand-name{font-family:"Ubuntu",sans-serif;font-weight:500;font-size:15px;color:var(--navy);text-transform:uppercase}
.title{position:absolute;left:0;width:718px;text-align:center;font-family:"Montserrat",sans-serif;font-weight:800;color:#fff;text-shadow:0 2px 4px rgba(0,0,0,.5)}
.title-line{top:330px;font-size:34px;line-height:40px}
.title-course{top:425px;font-size:35px;color:var(--orange)}
.title-sub{top:486px;font-family:"Tinos",serif;font-weight:700;font-size:28px;letter-spacing:.5px}
.intro{position:absolute;left:27px;top:626px;width:630px;color:#fff;font-size:13px;line-height:16px;text-align:justify}
.intro p+p{margin-top:6px}
.careers{position:absolute;left:0;top:779px;width:679px;height:59px;background:var(--orange);padding:7px 18px 0 31px;font-family:"Tinos",serif;font-size:12.6px;line-height:15px;color:#3a2a10;text-align:justify}
.contacts{position:absolute;left:31px;top:848px;font-size:12.5px;line-height:16px;color:#111}
.contacts li{list-style:none;display:flex;gap:12px;align-items:flex-start}
.contacts svg{flex:none;margin-top:2px}
.address{position:absolute;left:270px;top:848px;font-size:12.5px;line-height:15px;display:flex;gap:6px}
.follow{position:absolute;left:287px;top:910px;font-size:11px;font-weight:700;display:flex;align-items:center;gap:8px}
.social-name{font-size:13px;font-weight:500;color:var(--navy)}
.partner{position:absolute;left:530px;top:855px;display:flex;align-items:center;gap:8px}
.partner-dot{width:46px;height:46px;border-radius:50%;background:#d8264a}
.partner-name{font-size:20px;font-weight:500;color:#333}
.partner-cert{position:absolute;left:530px;top:905px;width:92px;height:14px;background:#e6e6e6}

/* right page */
.heading{position:absolute;display:flex;align-items:center;font-family:"Ubuntu",sans-serif;font-weight:700;font-size:19px;color:var(--navy)}
.heading span{color:var(--orange);margin-left:6px}
.mark{display:inline-block;width:34px;height:28px;background:linear-gradient(90deg,var(--navy) 0 70%,var(--orange) 70%);margin-right:11px}
.modules{position:absolute;left:704px;top:81px;width:627px;border-radius:6px;overflow:hidden;box-shadow:0 3px 8px rgba(0,0,0,.25);background:#fff}
.modules table{width:100%;border-collapse:collapse;font-size:12.5px}
.modules thead th{background:var(--navy);color:#fff;font-weight:400;font-size:16px;height:42px;border-bottom:5px solid var(--orange)}
.modules td{height:25.3px;border-right:4px solid #fff;border-top:1px solid #fff;padding:0 10px}
.modules td:nth-child(1){width:95px;padding-left:26px}
.modules td:nth-child(3){width:67px;text-align:center}
.modules td:nth-child(4){border-right:0;padding-left:16px}
.modules tr:nth-child(odd) td{background:var(--row-grey)}
.modules tr:nth-child(even) td{background:var(--orange)}
.modules tr:nth-child(even) td:nth-child(2),.modules tr:nth-child(even) td:nth-child(3){background:var(--orange-soft)}
.info{position:absolute;font-size:15px;line-height:19px;color:#222}
.info small{font-size:13.5px;line-height:17px}
.note{font-style:italic;font-size:15px;margin:8px 0 0 74px}
.entry{position:absolute;left:705px;top:684px;width:614px;height:228px;border:3px solid var(--orange);border-radius:8px;box-shadow:0 0 6px rgba(245,162,36,.5);padding:34px 8px 0 6px}
.entry-tab{position:absolute;left:18px;top:-13px;width:255px;height:24px;background:#fff;border:2px solid var(--orange);text-align:center;font-weight:500;font-size:17px;line-height:20px;color:var(--navy)}
.entry li{list-style:none;position:relative;padding-left:16px;font-size:14.2px;line-height:17px;margin-bottom:5px}
.entry li::before{content:"";position:absolute;left:2px;top:4px;width:10px;height:10px;border-radius:50%;background:var(--orange)}
.gst{position:absolute;right:47px;top:922px;font-style:italic;font-size:15px}
</style>
</head>
<body>
<div class="sheet">

  <section class="cover">
    <svg class="hero-art" width="679" height="779" viewBox="0 0 679 779">
      <defs>
        <radialGradient id="steel" cx="45%" cy="40%" r="65%">
          <stop offset="0" stop-color="#c9c9c9"/>
          <stop offset=".55" stop-color="#7c7c7c"/>
          <stop offset="1" stop-color="#1a1a1a"/>
        </radialGradient>
        <linearGradient id="sweep" x1="0" y1="0" x2="1" y2="1">
          <stop offset="0" stop-color="#2b3596"/>
          <stop offset="1" stop-color="var(--navy-deep)"/>
        </linearGradient>
      </defs>
      <path d="M0,95 C250,40 560,110 679,270 L679,779 L0,779 Z" fill="url(#sweep)"/>
      <path d="M0,80 C260,30 560,100 679,250" fill="none" stroke="var(--orange)" stroke-width="9"/>
      <ellipse cx="330" cy="330" rx="362" ry="270" fill="var(--orange-deep)"/>
      <ellipse cx="318" cy="320" rx="350" ry="258" fill="var(--orange)"/>
      <ellipse cx="312" cy="312" rx="342" ry="250" fill="url(#steel)" role="img" aria-label="Photograph of interlocking steel gears"/>
    </svg>

    <div class="brand">
      <div class="brand-dot"></div>
      <div class="brand-name">Brantwell College</div>
    </div>

    <h1 class="title title-line">HIGHER DIPLOMA<br>IN</h1>
    <div class="title title-course">MECHANICAL ENGINEERING</div>
    <div class="title title-sub">COURSE DESCRIPTION</div>

    <div class="intro">
      <p>Higher Diploma in Mechanical Engineering course emphasise design, analysis, and manufacturing new products and technologies. It addresses the society's needs by combining mechanical engineering fundamentals with innovative ideas. We structure our curriculum by emphasizing engineering theory and technical skills. Our students learn how to analyze solve practical problem.</p>
      <p>Mechanical Engineering provides a broad-based education that enables you to excel in diverse career choices. Its strong emphasis on applied design thinking skills gives you an edge in creating innovative solutions for using clean energy, developing new materials and processes, designing and manufacturing products that range from consumer products to construction equipment.</p>
    </div>

    <div class="careers">Graduates from this course can look forward to a career in Construction industry – designs and builds infrastructure, buildings and buildings services, Rail industry – design, construct, manage and maintain rail system components from trains and tracks to electrical power systems and train control systems.</div>

    <ul class="contacts">
      <li><svg width="16" height="12" viewBox="0 0 16 12"><path d="M1 4 Q8 -2 15 4 L13 6 L11 4 L5 4 L3 6 Z M4 6 h8 l2 5 h-12 Z" fill="#111"/></svg><b style="font-weight:500">+65 6200 1480, +65 9000 2741</b></li>
      <li style="margin-top:3px"><svg width="16" height="12" viewBox="0 0 16 12"><rect x="4" y="0" width="8" height="4" fill="#111"/><rect x="1" y="4" width="14" height="8" rx="1" fill="#111"/></svg>+65 6200 1481</li>
      <li style="margin-top:3px"><svg width="16" height="12" viewBox="0 0 16 12"><rect x="1" y="1" width="14" height="10" fill="none" stroke="#111"/><path d="M1 1 L8 7 L15 1 M1 11 L6 6 M15 11 L10 6" fill="none" stroke="#111"/></svg><span>info@brantwell.edu.sg<br>admissions@brantwell.edu.sg</span></li>
      <li style="margin-top:3px;padding-left:28px;font-size:13.5px">www.brantwell.edu.sg</li>
    </ul>

    <div class="address">
      <svg width="13" height="12" viewBox="0 0 13 12"><path d="M6.5 0 L13 6 H11 V12 H8 V8 H5 V12 H2 V6 H0 Z" fill="#111"/></svg>
      <span>48 Harbourview Road #03-08,<br>Block 2, Meridian Court,<br>Singapore 118420</span>
    </div>

    <div class="follow">Follow Us On <span class="social-name">Linkwave</span></div>

    <div class="partner">
      <div class="partner-dot"></div>
      <div class="partner-name">Learnsafe</div>
    </div>
    <div class="partner-cert"></div>
  </section>

  <h2 class="heading" style="left:679px;top:34px"><i class="mark"></i>MODULE<span>ASSESSMENT</span></h2>

  <div class="modules">
    <table>
      <thead><tr><th>HDME</th><th>MODULES</th><th>CREDITS</th><th>DISTRIBUTION</th></tr></thead>
      <tbody>
        <tr><td>IMP2o2</td><td>I IEP2oi Introduction to Electrical Principles</td><td>20</td><td>30% exam 70% Coursework</td></tr>
        <tr><td>FD2o3</td><td>Introduction to Mechanical Principles</td><td>20</td><td>100% coursework</td></tr>
        <tr><td>WSH2o4</td><td>Fluid Dynamics</td><td>20</td><td>100% coursework</td></tr>
        <tr><td>GEDA2o5</td><td>Workplace Safety and Health Practice</td><td>20</td><td>100% coursework</td></tr>
        <tr><td>PC2o6</td><td>Green Engineering Design and Application</td><td>20</td><td>100% coursework</td></tr>
        <tr><td>HTC3oi</td><td>Professions in Context</td><td>20</td><td>100% coursework</td></tr>
        <tr><td>AM3o2</td><td>Heat Transfer and Combustion</td><td>20</td><td>100% coursework</td></tr>
        <tr><td>RT3o3</td><td>Applied Mechanics</td><td>20</td><td>100% Examination</td></tr>
        <tr><td>CADA3o4</td><td>Robotics Technology</td><td>20</td><td>100% coursework</td></tr>
        <tr><td>MEM3o5</td><td>Computer Aided Design and Analysis</td><td>20</td><td>100% coursework</td></tr>
        <tr><td>PPP3o6</td><td>Material and Energy Management</td><td>20</td><td>100% coursework</td></tr>
        <tr><td></td><td>Professional Practice Project</td><td>20</td><td>100% coursework</td></tr>
      </tbody>
    </table>
  </div>

  <h2 class="heading" style="left:679px;top:492px"><i class="mark"></i>DURATION &amp;<span>TIME</span></h2>
  <div class="info" style="left:724px;top:523px">Full Time: 20 Months<br>Part Time: 24 Months<br>Sunday:9AM-5PM<br>Weekdays: 7PM-10PM<div class="note">*twice a week</div></div>

  <h2 class="heading" style="left:916px;top:492px"><i class="mark"></i>COURSE<span>FEE</span></h2>
  <div class="info" style="left:964px;top:527px"><small>Part Time<br>Full Payment: S$9,900*<br>Registration: S$100<br>Instalment: 2,12,24<br>months plan</small></div>

  <h2 class="heading" style="left:1133px;top:492px"><i class="mark"></i>AWARDED<span>BY</span></h2>
  <div class="info" style="left:1179px;top:530px"><small>Higher Diploma in<br>Mechanical Engineering<br>By Brantwell College</small></div>

  <h2 class="heading" style="left:1131px;top:597px"><i class="mark"></i>INTAKE</h2>
  <div class="info" style="left:1178px;top:631px"><small>Every 2 Months</small></div>

  <div class="entry">
    <div class="entry-tab">Entry Requirement</div>
    <ul>
      <li>Minimum 21 years and above.</li>
      <li>'A' Level 3 subjects passes. English plus any other subjects or; a related Diploma from local Polytechnic or; other CPE registered PEI or equivalent (Diplomas from other countries)</li>
      <li>IELTS 5.5 or equivalent</li>
      <li>Student with other diploma qualifications with minimum age of 23 years with at least 3 years working experience in relevant field. Recognition of Prior Learning (RPL) will be done to analysis whether student has met the required skills to be admitted onto our Higher Diplomas.</li>
      <li>Matured students, of 30 years old with at least 8 years of working experience will be considered on an individual basis.</li>
    </ul>
  </div>

  <div class="gst">*All fees excluding GST</div>
</div>
</body>
</html>
```